Business card for pediatric occupational therapist

I need a business card design for my independent occupational therapy company. I am a pediatric occupational therapist working with children 0-3 years of age. I would like the card to be clean (not too 'busy') and can include pictures/cartoon-like images of children, or toys such as building blocks, or other images that would be relevant to pediatric therapy. I want it to look professional but also intended to be clear that services provided are for children.
Target Market(s)
Families requiring occupational therapy services for their children (physical, emotional, social needs) - developmental delays
Industry/Entity Type
Rehabilitation
Contact Information for Business Card
Marisa Dunphrey OT LLC
Marisa Dunphrey, OTR/L
Occupational Therapist
marisa.dunphreyOT@brightmail.example

```html
<!DOCTYPE html>
<html lang="en">
<head>
<meta charset="utf-8">
<title>Marisa Dunphrey OT LLC — Business Card</title>
<link href="https://fonts.googleapis.com/css2?family=Montserrat:wght@600&family=Nunito+Sans:wght@300;400;900&display=swap" rel="stylesheet">
<style>
  :root {
    --green: #00c305;
    --charcoal: #373737;
    --white: #ffffff;
    --ink: #333333;
  }
  * { box-sizing: border-box; margin: 0; padding: 0; }
  html, body { width: 1200px; height: 765px; overflow: hidden; }
  body { position: relative; background: var(--green); font-family: "Nunito Sans", sans-serif; color: var(--ink); }

  .backdrop { position: absolute; inset: 0; width: 1200px; height: 765px; }

  .card {
    position: absolute;
    width: 520px;
    height: 297px;
    background: var(--white);
    overflow: hidden;
  }
  .card--front { left: 312px; top: 90px; }
  .card--back { left: 369px; top: 424px; }

  /* Front */
  .brand-square {
    position: absolute;
    left: 47px; top: 55px;
    width: 188px; height: 188px;
    background: var(--charcoal);
  }
  .brand-name {
    position: absolute;
    left: 260px; top: 148px;
    font-family: "Montserrat", sans-serif;
    font-weight: 600;
    font-size: 31px;
    line-height: 32.5px;
    font-variant: small-caps;
    color: var(--charcoal);
    letter-spacing: 0.2px;
  }

  /* Back */
  .back-square {
    position: absolute;
    left: 224px; top: 41px;
    width: 72px; height: 72px;
    background: var(--green);
  }
  .holder-name {
    position: absolute;
    left: 0; right: 0; top: 142px;
    text-align: center;
    font-size: 27px;
    line-height: 34px;
    color: var(--charcoal);
    letter-spacing: -0.3px;
  }
  .holder-name strong { font-weight: 900; }
  .holder-name span { font-weight: 400; }
  .holder-title {
    position: absolute;
    left: 0; right: 20px; top: 178px;
    text-align: center;
    font-weight: 300;
    font-size: 20px;
    color: var(--charcoal);
  }
  .contact {
    position: absolute;
    left: 0; right: 0; top: 241px;
    display: flex;
    justify-content: center;
    align-items: center;
    gap: 7px;
    font-size: 16.5px;
    font-weight: 400;
    color: var(--charcoal);
    letter-spacing: 0.3px;
  }
  .contact svg { width: 25px; height: 22px; flex: none; }
  .footer-band {
    position: absolute;
    left: 0; right: 0; bottom: 0;
    height: 26px;
    background: var(--green);
  }
</style>
</head>
<body>
  <svg class="backdrop" viewBox="0 0 1200 765" aria-hidden="true">
    <polygon points="0,678 1200,47 1200,765 0,765" fill="var(--charcoal)"/>
  </svg>

  <section class="card card--front">
    <div class="brand-square"></div>
    <p class="brand-name">Pediatric<br>Occupational<br>Therapist</p>
  </section>

  <section class="card card--back">
    <div class="back-square"></div>
    <h1 class="holder-name"><strong>Marisa Dunphrey</strong> <span>OT LLC</span></h1>
    <p class="holder-title">Occupational Therapist</p>
    <p class="contact">
      <svg viewBox="0 0 25 22" aria-hidden="true">
        <path d="M5 9V2h15v7" fill="none" stroke="var(--charcoal)" stroke-width="1.4"/>
        <path d="M1 8l11.5 8L24 8v13H1z" fill="var(--charcoal)"/>
        <path d="M1 21l9-7M24 21l-9-7" stroke="var(--white)" stroke-width="1.2"/>
        <circle cx="12.5" cy="6.5" r="2.3" fill="none" stroke="var(--charcoal)" stroke-width="1"/>
      </svg>
      <span>marisa.dunphreyOT@brightmail.example</span>
    </p>
    <div class="footer-band"></div>
  </section>
</body>
</html>
```